Design the web for "http://www.qlchatter.example"

QLChatter is an open source customer communication platform, think as BRAVOLINK.IO alternative.

QLChatter web site is an entry to let people know QLChatter and try QLChatter online QLChatter service.

1, To design the web site, suggest try QLChatter first.

2, At least replace the original pictures which QLChatter web site now use. (All got from cloudshelf site, shame and not reasonable)

3, Provide total web design, Picture and Code.

Thanks,
QLChatter owner
Haoran Wei
weihaoran@mailbox.example

Reason: So far no useful design, and only five designers submit their designs. And one man submit 48 designs, most of his design is same style. I request to extend the deadline, and invite more designers. Thanks, Haoran

Target Market(s)

Open Source.

Industry/Entity Type

Software

Coding

Coded - Design and coding required

Number of Pages Required

2 page

Font styles to use
Sans Serif

Requirements
Must have
• 1) Try QLChatter first
• 2) Replace all the pictures in the current site.
• 3) Match with the QLChattr features (Customer Communication / Open Source / Open API etc.)
• 4) Download page presents QLChatter support all kinds of platforms since QLChatter has all kinds of application for different OS.
• 5) Web style tuning (The current style copy from cloudshelf)
• 6) All pictures and web code.
Nice to have
• 1) Logo tuning for the new web style and logo file attached.
• 2) Extremely simple style is prefer.

```html
<!DOCTYPE html>
<html lang="en">
<head>
<meta charset="utf-8">
<title>QLChatter — Open Source Customer Communication Platform</title>
<link rel="stylesheet" href="https://fonts.googleapis.com/css2?family=Open+Sans:wght@400;600;700&display=swap">
<style>
:root{
  --navy:#0f3343;
  --navy-deep:#0b2a38;
  --cyan:#4ec3d8;
  --cyan-dark:#3fa9bd;
  --ink:#1c2b33;
  --body:#6b6b6b;
  --footer:#333336;
  --field:#4a4a4d;
  --white:#ffffff;
}
*{box-sizing:border-box;margin:0;padding:0}
html,body{width:704px;height:1200px;overflow:hidden}
body{font-family:"Open Sans",Arial,sans-serif;background:var(--white);position:relative;color:var(--ink)}

/* header */
.site-header{position:absolute;left:0;top:0;width:704px;height:64px;background:var(--navy);border-top:2px solid var(--cyan)}
.brand{position:absolute;left:58px;top:19px;display:flex;align-items:center;gap:6px;color:var(--white);font-weight:600;font-size:20px;letter-spacing:-.3px}
.brand-mark{width:24px;height:24px;background:var(--cyan);border-radius:3px}
.main-nav{position:absolute;right:74px;top:27px;display:flex;font-size:7px;color:var(--white);letter-spacing:.2px}
.main-nav a{color:inherit;text-decoration:none}
.main-nav a.active{color:var(--cyan)}
.main-nav .sep{color:var(--cyan);margin:0 22px}
.search-icon{position:absolute;right:58px;top:26px}

/* hero */
.hero{position:absolute;left:0;top:64px;width:704px;height:292px;background:linear-gradient(100deg,#9eb0bd 0%,#7f96a8 35%,#5f7f98 55%,#a9b6c0 80%,#c5ccd2 100%)}
.hero-title{position:absolute;left:58px;top:86px;font-size:24px;font-weight:700;color:var(--white);letter-spacing:.4px}
.hero-sub{position:absolute;left:58px;top:121px;font-size:13.5px;font-weight:400;color:var(--white);letter-spacing:.2px}
.hero-rule{position:absolute;left:58px;top:152px;width:144px;height:2px;background:var(--white)}
.hero-rule::before{content:"";position:absolute;left:0;top:0;width:74px;height:2px;background:var(--cyan)}
.hero-text{position:absolute;left:58px;top:166px;width:330px;font-size:7.6px;line-height:14px;color:var(--white)}
.hero-dots{position:absolute;left:57px;top:207px;display:flex;gap:5px}
.hero-dots span{width:8px;height:8px;border-radius:50%;border:1px solid var(--cyan)}
.hero-dots span.on{background:var(--cyan)}

/* about */
.about-media{position:absolute;left:58px;top:384px;width:196px;height:142px;border-radius:4px;background:linear-gradient(135deg,#2d5f7c,#6fa7c4 55%,#1f4660)}
.about-stand{position:absolute;left:126px;top:526px;width:60px;height:22px;background:linear-gradient(#d8d8d8,#b9b9b9);clip-path:polygon(20% 0,80% 0,95% 100%,5% 100%)}
.section-title{font-size:13.5px;font-weight:700;color:var(--ink);letter-spacing:.2px}
.section-title em{font-style:normal;color:var(--cyan)}
.about-title{position:absolute;left:300px;top:380px}
.about-lead{position:absolute;left:299px;top:405px;font-size:6.6px;color:#444;letter-spacing:.1px}
.about-copy{position:absolute;left:300px;top:425px;width:350px;font-size:5.8px;line-height:13px;color:var(--body)}
.about-copy p{margin-bottom:8.5px}
.btn{display:inline-block;background:var(--cyan);color:var(--white);font-weight:700;text-decoration:none;text-align:center}
.about-btn{position:absolute;left:301px;top:525px;width:77px;height:26px;line-height:26px;font-size:8.5px;border-bottom:2px solid var(--cyan-dark)}

/* features */
.features{position:absolute;left:0;top:576px;width:704px;height:299px;overflow:hidden;background:linear-gradient(90deg,#2f4a5c 0%,#3d5a6d 35%,#2d4a5e 60%,#3a5568 100%)}
.features-media{position:absolute;left:56px;top:40px;width:184px;height:259px;border-radius:30px 30px 0 0;background:linear-gradient(160deg,#c9d3d9,#9fb5c1 45%,#c8b6a5 80%)}
.features-title{position:absolute;left:311px;top:44px;color:var(--white)}
.timeline{position:absolute;left:332px;top:106px;width:2px;height:142px;background:var(--navy-deep)}
.feature-icon{position:absolute;left:312px;width:42px;height:42px;border-radius:50%;background:var(--white);border:3px solid var(--navy-deep);display:flex;align-items:center;justify-content:center}
.feature-icon.active{border-color:var(--cyan);box-shadow:0 0 0 2px rgba(78,195,216,.35)}
.feature{position:absolute;left:367px;width:290px;color:var(--white)}
.feature h3{font-size:7.6px;font-weight:600;letter-spacing:.2px;white-space:nowrap}
.feature h3.active{color:var(--cyan)}
.feature p{font-size:6.2px;line-height:12.5px;margin-top:3px;font-family:Arial,sans-serif}

/* updates */
.updates-title{position:absolute;left:58px;top:893px}
.update{position:absolute;top:925px;width:190px}
.update-date{position:absolute;left:0;top:0;color:#555;font-weight:600;font-size:16px;line-height:16px}
.update-date small{display:block;font-size:11px;margin-top:3px}
.update-date.active{color:var(--cyan)}
.update h4{position:absolute;left:30px;top:3px;font-size:7px;font-weight:400;color:#333;white-space:nowrap}
.update h4.active{color:var(--cyan)}
.update p{position:absolute;left:30px;top:18px;width:160px;font-size:5.8px;line-height:12px;color:#888}

/* footer */
.site-footer{position:absolute;left:0;top:1004px;width:704px;height:160px;background:var(--footer);color:var(--white)}
.footer-head{position:absolute;top:32px;font-size:10.5px;font-weight:400}
.field{position:absolute;left:58px;width:120px;height:19px;background:var(--field);font-size:6.5px;color:#9a9a9a;padding:6px 10px}
.field-msg{left:187px;top:59px;width:119px;height:47px}
.submit{position:absolute;left:187px;top:114px;width:53px;height:19px;line-height:19px;font-size:7px;font-weight:600}
.footer-copy{position:absolute;left:346px;top:55px;width:226px;font-size:6px;line-height:12px;color:#8c8c8c}
.social{position:absolute;left:347px;top:130px;font-size:7.5px;display:flex;align-items:center;gap:6px}
.social span{width:16px;height:16px;border-radius:50%;background:#6d6d70}
.footer-links{position:absolute;left:598px;top:55px;list-style:none;font-size:6px;line-height:14.5px;color:#9a9a9a}
.bottom-bar{position:absolute;left:0;top:1164px;width:704px;height:36px;background:var(--cyan);text-align:center;font-size:6px;color:var(--white);line-height:36px}
</style>
</head>
<body>

<header class="site-header">
  <div class="brand"><span class="brand-mark"></span>qlchatter</div>
  <nav class="main-nav">
    <a href="#" class="active">HOME</a><span class="sep">⋮</span>
    <a href="#">DOCUMENTATION</a><span class="sep">⋮</span>
    <a href="#">DOWNLOAD</a><span class="sep">⋮</span>
  </nav>
  <svg class="search-icon" width="9" height="9" viewBox="0 0 10 10"><circle cx="4" cy="4" r="3" fill="none" stroke="#4ec3d8" stroke-width="1.6"/><line x1="6.2" y1="6.2" x2="9" y2="9" stroke="#4ec3d8" stroke-width="1.8"/></svg>
</header>

<section class="hero" role="img" aria-label="Blurred photo of a hand holding a smartphone">
  <h1 class="hero-title">OPEN SOURCE PLUG &amp; PLAY</h1>
  <h2 class="hero-sub">CUSTOMER COMMUNICATION PLATFORM</h2>
  <div class="hero-rule"></div>
  <p class="hero-text">Sed ut perspiciatis unde omnis iste natus error sit voluptatem accusantium doloremque laudantium, totam rem aperiam, eaque ipsa quae ab illo inventore veritatis</p>
  <div class="hero-dots"><span class="on"></span><span></span><span></span></div>
</section>

<section class="about">
  <div class="about-media" role="img" aria-label="Desktop monitor showing a hand touching floating app icons"></div>
  <div class="about-stand"></div>
  <h2 class="section-title about-title">ABOUT <em>QLCHATTER</em></h2>
  <p class="about-lead">SIMPLY DUMMY TEXT OF THE PRINTING AND TYPESETTING INDUSTRY. LOREM IPSUM</p>
  <div class="about-copy">
    <p>Lorem Ipsum is simply dummy text of the printing and typesetting industry. Lorem Ipsum has been the industry's standard dummy text ever since the 1500s, when an unknown printer took a galley of type and scrambled it to make a type specimen book. It has survived not only five centuries.</p>
    <p>Dummy text ever since the 1500s, when denouncing pleasure and praising pain was born and I will give you a complete</p>
    <p>account of the system, and expoundan unknown printer took a galley of type and scrambled it to make a type specimen book. It has survived not only five centuries...</p>
  </div>
  <a href="#" class="btn about-btn">VIEW MORE</a>
</section>

<section class="features">
  <div class="features-media" role="img" aria-label="Hand holding a smartphone showing the QLChatter site"></div>
  <h2 class="section-title features-title">QLCHATTR <em>FEATURES</em></h2>
  <div class="timeline"></div>

  <div class="feature-icon active" style="top:85px">
    <svg width="12" height="14" viewBox="0 0 12 14"><rect x="2.5" y="0.8" width="7" height="12.4" rx="1.2" fill="none" stroke="#0b2a38" stroke-width="1.3"/><circle cx="6" cy="11" r=".8" fill="#0b2a38"/></svg>
  </div>
  <div class="feature" style="top:86px"><h3 class="active">LOREM IPSUM IS SIMPLY DUMMY</h3><p>Lorem Ipsum is simply dummy text of the printing and typesetting industry. Lorem Ipsum hasNe que porro quisquam est, been the industry's...</p></div>

  <div class="feature-icon" style="top:156px">
    <svg width="14" height="14" viewBox="0 0 14 14"><circle cx="7" cy="7" r="5.5" fill="none" stroke="#0b2a38" stroke-width="1.5"/><path d="M7 4v3.3h2.4" fill="none" stroke="#0b2a38" stroke-width="1.3"/></svg>
  </div>
  <div class="feature" style="top:157px"><h3>LOREM IPSUM IS SIMPLY DUMMY</h3><p>Lorem Ipsum is simply dummy text of the printing and typesetting industry. Lorem Ipsum hasNe que porro quisquam est, been the industry's...</p></div>

  <div class="feature-icon" style="top:226px">
    <svg width="14" height="14" viewBox="0 0 14 14"><path d="M2 12l5.5-5.5" stroke="#0b2a38" stroke-width="2.2" stroke-linecap="round"/><circle cx="9.5" cy="4.5" r="3" fill="#0b2a38"/><circle cx="11" cy="3" r="1.3" fill="#fff"/></svg>
  </div>
  <div class="feature" style="top:227px"><h3>LOREM IPSUM IS SIMPLY DUMMY</h3><p>Lorem Ipsum is simply dummy text of the printing and typesetting industry. Lorem Ipsum hasNe que porro quisquam est, been the industry's...</p></div>
</section>

<section class="updates">
  <h2 class="section-title updates-title"><em>RECENT</em> UPDATES</h2>
  <article class="update" style="left:58px">
    <div class="update-date active">17<small>/16</small></div>
    <h4 class="active">On the other hand, we denounce</h4>
    <p>At vero eos et accusamus et iusto odio dignissimos ducimus qui blanditiis praesentium voluptatum deleniti dolores et quas molestias excepturi</p>
  </article>
  <article class="update" style="left:258px">
    <div class="update-date">14<small>/16</small></div>
    <h4>On the other hand, we denounce</h4>
    <p>At vero eos et accusamus et iusto odio dignissimos ducimus qui blanditiis praesentium voluptatum deleniti dolores et quas molestias excepturi</p>
  </article>
  <article class="update" style="left:464px">
    <div class="update-date">12<small>/16</small></div>
    <h4>On the other hand, we denounce</h4>
    <p>At vero eos et accusamus et iusto odio dignissimos ducimus qui blanditiis praesentium voluptatum deleniti dolores et quas molestias excepturi</p>
  </article>
</section>

<footer class="site-footer">
  <h3 class="footer-head" style="left:58px">Contact us</h3>
  <div class="field" style="top:59px">Name</div>
  <div class="field" style="top:86px">Email Address</div>
  <div class="field" style="top:114px">Website Address</div>
  <div class="field field-msg">Messages</div>
  <a href="#" class="btn submit">SUBMIT</a>

  <h3 class="footer-head" style="left:346px">At vero eos et accusamus</h3>
  <p class="footer-copy">At vero eos et accusamus et iusto odio dignissimos ducimus qui blanditiis praesentium voluptatum deleniti atque corrupti quos dolores et quas molestias excepturi sint occaecati cupiditate non provident, Nam libero tempore, cum soluta nobis est eligendi optio cumque nihil impedit quo minus id quod maxime placeat facere possimus,</p>
  <div class="social">Connect with our social network :<span></span><span></span><span></span></div>

  <h3 class="footer-head" style="left:597px">Welcome</h3>
  <ul class="footer-links"><li>Home</li><li>Services</li><li>About us</li><li>Product</li><li>Contact Us</li></ul>
</footer>

<div class="bottom-bar">Copyright © 2016, QLChatter  all right reseved.</div>

</body>
</html>
```